Company van wrap design.

We are The Drain Restore Group - We are looking to have our Varlon Haulmax wrapped/stickered, and need the expertise of a GD.

We have included an image of our current car that has been wrapped previously with the images supplied below. essentially we are after the same design in a bigger scale for our new company van.

Below is the logo and photos of the van.
1. We require our images to be amended to suit our vehicle.

2. These images MUST be clean and pop! NO BACKGROUND effects - eg see images attached - we do not want any background imagery simply the images we have supplied below.

3. We would like to include the Chatterbook and Snapgrid logo.

4. The back of the van will have the pipe running around the top also. We require the logo contact number and website to be included on all sides.

We are looking for our van to be designed to look as similar as our current vehicle. (No drastic changes)

Our new car is black. previously we have needed a wrap design but seeing as this car is black can this just be sticker designs?

The Car is a 2022 Varlon Haulmax.
Color: black

We look forward to receiving your work!

Smiles
Marisol

```html
<!DOCTYPE html>
<html lang="en">
<head>
<meta charset="utf-8">
<title>The Drain Restore Group – Van Side Graphics</title>
<link rel="stylesheet" href="https://fonts.googleapis.com/css2?family=Exo+2:wght@500;600&family=Montserrat:wght@600;700;800&display=swap">
<style>
  :root {
    --page: #ffffff;
    --van-black: #0b0b0c;
    --van-trim: #1f1f22;
    --glass: #3a4048;
    --stripe-grey: #3b3c40;
    --teal: #3aa39a;
    --teal-light: #7fd0c4;
    --mint: #9fd9a8;
    --white: #ffffff;
    --copper: #d99a6c;
    --copper-dark: #8a5a3a;
    --tyre: #1a1a1a;
    --rim: #8d9095;
    --lamp-red: #b8262b;
    --lamp-clear: #d9dde2;
  }
  html, body {
    margin: 0;
    padding: 0;
    width: 1200px;
    height: 1200px;
    overflow: hidden;
    background: var(--page);
  }
  .van-sheet {
    display: block;
    width: 1200px;
    height: 1200px;
  }
  .label-small { font-family: "Montserrat", sans-serif; font-weight: 700; font-size: 11px; fill: var(--white); }
  .brand-name { font-family: "Exo 2", sans-serif; font-weight: 500; font-size: 17px; fill: var(--white); letter-spacing: 0.3px; }
  .brand-tagline { font-family: "Exo 2", sans-serif; font-weight: 500; font-size: 6px; fill: var(--white); letter-spacing: 0.4px; }
  .service-item { font-family: "Exo 2", sans-serif; font-weight: 600; font-size: 16px; fill: var(--white); letter-spacing: 0.3px; }
  .phone-number { font-family: "Montserrat", sans-serif; font-weight: 700; font-size: 27px; fill: var(--white); }
  .web-address { font-family: "Montserrat", sans-serif; font-weight: 700; font-size: 18px; fill: var(--white); }
  .social-name { font-family: "Exo 2", sans-serif; font-weight: 600; font-size: 8px; fill: var(--white); }
</style>
</head>
<body>
<svg class="van-sheet" viewBox="0 0 960 960" xmlns="http://www.w3.org/2000/svg">
  <defs>
    <linearGradient id="pipe-before-tone" x1="0" y1="0" x2="0" y2="1">
      <stop offset="0" stop-color="#e7b48c"/>
      <stop offset="0.5" stop-color="var(--copper)"/>
      <stop offset="1" stop-color="var(--copper-dark)"/>
    </linearGradient>
    <linearGradient id="pipe-after-tone" x1="0" y1="0" x2="1" y2="0">
      <stop offset="0" stop-color="var(--teal-light)"/>
      <stop offset="0.35" stop-color="#d9a57c"/>
      <stop offset="1" stop-color="var(--copper)"/>
    </linearGradient>
  </defs>

  <!-- van body -->
  <g class="van-body">
    <path d="M66 590 L66 310 Q68 282 98 280 L585 279 Q612 280 630 292 L705 335 Q740 360 770 400 L850 448 Q885 462 890 490 L895 595 Q894 606 880 607 L66 607 Z" fill="var(--van-black)"/>
    <path d="M66 540 L895 540 L895 600 Q894 606 880 607 L66 607 Z" fill="var(--van-trim)"/>
    <path d="M572 336 L628 336 Q650 338 668 350 L712 392 Q722 410 712 446 L585 446 Q572 446 572 432 Z" fill="var(--glass)"/>
    <rect x="66" y="448" width="8" height="62" rx="3" fill="var(--lamp-red)"/>
    <path d="M832 462 L878 470 Q888 480 886 500 L848 494 Z" fill="var(--lamp-clear)"/>
  </g>

  <!-- wheels -->
  <g class="wheels">
    <circle cx="203" cy="598" r="58" fill="var(--van-black)"/>
    <circle cx="203" cy="598" r="50" fill="var(--tyre)"/>
    <circle cx="203" cy="598" r="30" fill="var(--rim)"/>
    <circle cx="775" cy="596" r="58" fill="var(--van-black)"/>
    <circle cx="775" cy="596" r="50" fill="var(--tyre)"/>
    <circle cx="775" cy="596" r="30" fill="var(--rim)"/>
  </g>

  <!-- before / after pipe imagery -->
  <g class="pipe-comparison">
    <rect x="86" y="312" width="214" height="56" rx="10" fill="url(#pipe-before-tone)" role="img" aria-label="Illustration of a cracked clay pipe with tree roots growing through it"/>
    <text class="label-small" x="237" y="382" text-anchor="middle">BEFORE</text>
    <rect x="322" y="312" width="236" height="50" rx="10" fill="url(#pipe-after-tone)" role="img" aria-label="Illustration of the same pipe restored with a smooth teal inner lining"/>
    <text class="label-small" x="412" y="384" text-anchor="middle">AFTER</text>
  </g>

  <!-- brand block -->
  <g class="brand-block">
    <circle cx="180" cy="432" r="38" fill="var(--teal)"/>
    <text class="brand-name" x="228" y="414">THE DRAIN</text>
    <text class="brand-name" x="228" y="432">RESTORE</text>
    <text class="brand-name" x="228" y="450">GROUP</text>
    <line x1="228" y1="457" x2="304" y2="457" stroke="var(--white)" stroke-width="0.8"/>
    <text class="brand-tagline" x="228" y="466">NO DIG PIPE REPAIRS</text>
  </g>

  <!-- services list -->
  <g class="service-list">
    <circle cx="352" cy="407" r="4" fill="none" stroke="var(--mint)" stroke-width="2.2"/>
    <text class="service-item" x="366" y="413">BLOCKED DRAINS</text>
    <circle cx="352" cy="424" r="4" fill="none" stroke="var(--mint)" stroke-width="2.2"/>
    <text class="service-item" x="366" y="430">CCTV INSPECTIONS</text>
    <circle cx="352" cy="441" r="4" fill="none" stroke="var(--mint)" stroke-width="2.2"/>
    <text class="service-item" x="366" y="447">PIPE RELINING</text>
    <circle cx="352" cy="459" r="4" fill="none" stroke="var(--mint)" stroke-width="2.2"/>
    <text class="service-item" x="366" y="465">PIPE COATING</text>
  </g>

  <!-- contact stripe -->
  <g class="contact-stripe">
    <path d="M68 481 L333 481 L318 512 L68 512 Z" fill="var(--stripe-grey)"/>
    <path d="M345 483 L850 483 L850 512 L331 512 Z" fill="var(--teal)"/>
    <text class="phone-number" x="156" y="507">55512047</text>
    <text class="web-address" x="356" y="504">www.thedrg.com.au</text>
  </g>

  <!-- social handles -->
  <g class="social-links">
    <rect x="614" y="486" width="12" height="12" rx="2" fill="var(--white)"/>
    <text class="social-name" x="614" y="508">Snapgrid</text>
    <circle cx="660" cy="492" r="6" fill="var(--white)"/>
    <text class="social-name" x="648" y="508">Chatterbook</text>
  </g>
</svg>
</body>
</html>
```